The WILLOW Lodge is a transitional living housue for women in recovery. It is structured and loving an

I have uploaded my old brochure which was not designed professionally. I want a fresh, funky feel. Our website is www.willowlodgeofthecedarshores.com if you want to get ideas from that but I do not like the bubbles on it. I have uploded a few pics of the houses and the backyards. Please help us convey love and hope and recovery!

```html
<!DOCTYPE html>
<html lang="en">
<head>
<meta charset="utf-8">
<title>WILLOW Lodge – Recovery Homes for Women Brochure</title>
<link href="https://fonts.googleapis.com/css2?family=Arimo:wght@400;700&display=swap" rel="stylesheet">
<style>
  :root{
    --purple:#7d3f9c;
    --purple-deep:#5c2a7d;
    --purple-soft:#a46cc2;
    --yellow:#f3ec34;
    --ink:#1f1a24;
    --paper:#ffffff;
    --backdrop:#e9e6ee;
  }
  *{box-sizing:border-box;margin:0;padding:0}
  html,body{width:900px;height:1200px;overflow:hidden}
  body{background:var(--backdrop);font-family:"Arimo",Arial,sans-serif;color:var(--ink);padding:20px 18px;display:flex;flex-direction:column;gap:20px}
  .spread{width:864px;height:570px;display:grid;grid-template-columns:repeat(3,288px);box-shadow:0 2px 10px rgba(0,0,0,.18)}
  .panel{position:relative;overflow:hidden;background:var(--paper)}
  .photo{display:block}
  .tab{background:var(--purple);color:#fff;font-weight:700;text-transform:uppercase;letter-spacing:.5px}
  .brand{color:var(--yellow);font-weight:700}
  p{font-size:10.5px;line-height:1.32;text-align:justify}

  /* outside: back panel */
  .back{padding:24px 16px 0}
  .back .tab{font-size:17px;padding:7px 12px;margin:0 -4px 10px}
  .back .tab span{color:var(--yellow)}
  .back .photo{width:256px;height:170px;margin:10px 0 12px;background:linear-gradient(160deg,#9fbf6b,#3f6a2c 55%,#7d6a4c)}
  .pill{background:var(--yellow);color:var(--purple);font-weight:700;text-align:center;border-radius:20px;font-size:11px;line-height:1.25;padding:6px 14px}
  .back .brand-band{background:var(--purple);margin:10px -16px 0;padding:12px 0;text-align:center;font-size:30px}
  .web-bar{background:var(--purple);color:#fff;text-align:center;font-size:10.5px;padding:6px 0;margin:8px -16px 0}

  /* outside: middle panel */
  .treat{display:flex;flex-direction:column}
  .treat .photo{width:288px;height:180px;background:linear-gradient(180deg,#4f7a3c,#6aa0b8 55%,#2f9be0)}
  .treat .body{background:var(--purple);color:#fff;flex:1;padding:16px 18px 10px;font-size:10.5px}
  .treat h3{font-size:11.5px;line-height:1.25;margin-bottom:4px}
  .treat ol{list-style:none;font-size:10.5px;line-height:1.35;margin-bottom:6px}
  .treat p{color:#fff;margin-bottom:10px}
  .treat ul{list-style:none;font-size:10.5px;line-height:1.4}
  .treat ul li::before{content:"";display:inline-block;width:7px;height:7px;border-radius:50%;background:var(--yellow);margin-right:7px}
  .footer-contact{font-size:8px;line-height:1.5;color:var(--yellow);margin-top:12px;border-top:1px solid var(--purple-soft);padding-top:6px}

  /* outside: cover */
  .cover{padding:22px 16px 0;text-align:center}
  .cover .tab{font-size:28px;padding:6px 0;margin:0 -16px 10px}
  .cover .photo{width:256px;height:200px;margin:0 auto 14px;background:linear-gradient(150deg,#c9e7d6,#86b66a 45%,#3d6d34)}
  .cover .region{color:var(--purple);font-size:14px;font-weight:700;line-height:1.1}
  .cover .headline{color:var(--purple);font-size:22px;font-weight:700;line-height:1.05}
  .cover .sub{color:var(--purple);font-size:14px;font-weight:700;margin-bottom:12px}
  .cover .pill{font-size:15px;padding:8px 10px}
  .cover .loc{background:var(--purple);color:#fff;font-size:11px;text-align:right;padding:6px 12px;margin:12px -16px 4px}
  .cover .phone{background:var(--purple);color:#fff;font-size:19px;font-weight:700;padding:5px 0;margin:0 -16px 4px;display:flex;align-items:center;justify-content:center;gap:8px}
  .cover .web{color:var(--purple);font-size:9.5px}

  /* inside */
  .inside{background:linear-gradient(90deg,var(--purple-deep),var(--purple) 50%,var(--purple-deep))}
  .inside .panel{background:transparent;padding:14px 10px}
  .card{background:var(--paper);border-radius:10px;height:100%;overflow:hidden;display:flex;flex-direction:column}
  .card .photo{height:185px;flex:none}
  .living .photo{background:linear-gradient(170deg,#6f8a4f,#3c5a2d 60%,#8aa06a)}
  .overview .photo{background:linear-gradient(180deg,#b9d3ea,#6e7f93 55%,#e7e7e7)}
  .card .tab{font-size:15px;text-align:center;padding:6px 0;margin:10px 14px 8px}
  .card .text{padding:0 14px}
  .card .text p{margin-bottom:8px}
  .section h4{color:var(--purple);font-size:12px;text-transform:uppercase;border-bottom:1.5px solid var(--purple-soft);margin-bottom:3px;padding-bottom:1px}
  .section p{font-size:9.6px;line-height:1.28;margin-bottom:6px}
  .info .card{padding:14px 14px}
  .info .section p{font-size:9.4px;margin-bottom:5px}
</style>
</head>
<body>

<section class="spread outside">
  <div class="panel back">
    <h2 class="tab">Sisters <span>&amp;</span> Supports</h2>
    <p>The WILLOW Lodge is known for creating an instant support system for those in early recovery. We have developed a HARBOR House to offer our recovering sisters after they have completed their goals at the WILLOW Lodge. It's a self-managed home with a lower rent, designed for women to save money and practice living on their own! We reinforce the benefits of healthy interdependency upon women in recovery and offer beautiful, serene, and safe housing for women to live and visit. No one ever has to be alone during early recovery.</p>
    <div class="photo" role="img" aria-label="Photo of a wooden garden walkway through lush tropical plants"></div>
    <div class="pill">We are located close to Gulf Coast beaches, parks, churches, shopping and schools.</div>
    <div class="brand-band"><span class="brand">WILLOW Lodge</span></div>
    <div class="web-bar">www.willowlodgeofthecedarshores.com</div>
  </div>

  <div class="panel treat">
    <div class="photo" role="img" aria-label="Photo of a backyard swimming pool surrounded by palms"></div>
    <div class="body">
      <h3>We recognize the multiple benefits of treatment programs:</h3>
      <ol>
        <li>1) professional case management</li>
        <li>2) individual therapy</li>
        <li>3) group therapy and</li>
        <li>4) education</li>
      </ol>
      <p>Once determined a woman is a proper fit for one of our houses, we are committed to reinforcing the individualized plan recommended by her treatment center and will work in conjunction with the center's staff.</p>
      <h3>We offer additional guidance on an individual basis which may include:</h3>
      <ul>
        <li>Relapse Prevention</li>
        <li>Financial management/budgeting</li>
        <li>Resume writing &amp; Job coaching</li>
        <li>Case management</li>
        <li>Medication monitoring</li>
        <li>Recovery coaching</li>
      </ul>
      <div class="footer-contact">WILLOW Lodge of the Cedar Shores<br>(555) 013-4820<br>info@willowlodgeofthecedarshores.com</div>
    </div>
  </div>

  <div class="panel cover">
    <h1 class="tab"><span class="brand">WILLOW Lodge</span></h1>
    <div class="photo" role="img" aria-label="Photo of a colourful cottage with a white picket fence and garden"></div>
    <div class="region">GULF COAST</div>
    <div class="headline">RECOVERY HOMES</div>
    <div class="sub">FOR WOMEN</div>
    <div class="pill">WILLOW LODGE<br>OF THE CEDAR SHORES</div>
    <div class="loc">Cedar Bay, FL</div>
    <div class="phone">
      <svg width="20" height="20" viewBox="0 0 20 20" aria-hidden="true"><circle cx="10" cy="10" r="9" fill="none" stroke="#fff" stroke-width="1.5"/><path d="M7 5.5c-.8.4-1.3 1.3-1 2.4.7 2.8 3 5.2 5.8 6 1 .3 2-.2 2.4-1l-1.8-1.6-1.2.7c-1.2-.6-2.2-1.6-2.8-2.8l.7-1.2z" fill="#fff"/></svg>
      (555) 013-4820
    </div>
    <div class="web">www.willowlodgeofthecedarshores.com</div>
  </div>
</section>

<section class="spread inside">
  <div class="panel living">
    <div class="card">
      <div class="photo" role="img" aria-label="Photo of a garden pond with lily pads and plants"></div>
      <h2 class="tab">Living in Recovery</h2>
      <div class="text">
        <p>The WILLOW Lodge was created to offer women a place to practice using their newly acquired sober living skills within the safety of a managed, independent living environment. We guide women into their foundation of a twelve-step program and reinforce the necessity of the life saving tools.</p>
        <p>We encourage women to incorporate the spiritual principles of the twelve steps into all of her affairs. This gives women a chance to become strong in her recovery before returning home or embarking on a new adult life.</p>
        <p>The communities are beautiful and serene. While we teach discipline, life skills, and work habits, we also teach the values of honesty, worthiness, and self-esteem. We provide comfortable and aesthetically appealing homes of which the women are proud to be a part.</p>
      </div>
    </div>
  </div>

  <div class="panel overview">
    <div class="card">
      <div class="photo" role="img" aria-label="Photo of a grey bungalow with a red door and white picket fence"></div>
      <h2 class="tab">Overview</h2>
      <div class="text">
        <div class="section"><h4>Living Skills</h4><p>We hold a mandatory weekly living skills meeting where house issues are solved. We learn in recovery that basic living skills are a necessary discipline, help build self-esteem, and help us learn accountability.</p></div>
        <div class="section"><h4>Relapse Prevention</h4><p>We offer a mandatory weekly relapse prevention group. Alumni are encouraged to continue this group after they have left the house.</p></div>
        <div class="section"><h4>Group Activities</h4><p>We encourage women to get involved with the sober communities by participating and/or serving in organized events.</p></div>
        <div class="section"><h4>Resource Center</h4><p>We offer a house computer, phone and internet access. We also have resume writing software and computer software tutorials for those new to computers or rusty in old skills.</p></div>
      </div>
    </div>
  </div>

  <div class="panel info">
    <div class="card">
      <div class="section"><h4>Location</h4><p>Residences are closely located to recovery club houses and many church meetings. Additionally, there is easy access to public transportation.</p></div>
      <div class="section"><h4>Healthcare &amp; Healing</h4><p>We have developed a network of reputable healing specialists in the areas to meet individual needs.</p></div>
      <div class="section"><h4>Social Services</h4><p>Managers have thorough knowledge of social services in local areas. Some women may be eligible for assistance.</p></div>
      <div class="section"><h4>In-House Managers</h4><p>Property Managers are in recovery. They also have experience in many areas of addiction related problems and remain mindful of issues that may arise during this time. Managers address the issues efficiently and with the appropriate people.</p></div>
      <div class="section"><h4>Mind, Body, &amp; Spirit</h4><p>Living clean and sober is a process. We encourage healing on all levels.</p></div>
      <div class="section"><h4>Senior Sister System</h4><p>We encourage the women with more clean time to take on a lead position of responsibility in the houses. It enables women to be accountable to one another and not just authority figures.</p></div>
      <div class="section"><h4>Your Responsibility</h4><p>You are responsible for making a decision to stay clean and sober, packing a bag, and moving in! We supply linens, towels, cleaning and paper products.</p></div>
    </div>
  </div>
</section>

</body>
</html>
```